Website for Plumbing Company, Sir FlowBoiler

I need a 7-page fully HTML-coded website for my plumbing company, Sir FlowBoiler. We specialize in installation, repair, and replacement of both gas and electric water heaters. Although we offer both tankless (on-demand) water heaters and standard (with tank) water heaters, most of our business is related to standard (with tank) water heaters in the USA market.

These are the pages I need:
1. Home page with sections such as About Us, Our Services, Why Choose Us, Testimonials, Location Map (Palm Beach County Florida), Quote Request Form, Join Our Newsletter, Mission Statement, etc.

2. Gas Water Heaters

3. Electric Water Heaters

4. Tankless Water Heaters

5. About Us

6. Contact Us

7. Privacy Policy, Terms & Conditions

Be sure to mention the following points:
1. Same-Day Service
2. Best Price Guarantee
3. 100% Satisfaction Rating
4. 15-Year Warranty on Water Heater & Parts
5. Lifetime Warranty on Workmanship
*All Warranties are Transferrable Upon Home Sale

Once design is selected and finalized, I need the website coded in a standard HTML/CSS and temporarily hosted on your development server so I can see the website functionality that is not observable from screenshots, such as section animations, etc. Once those details are finalized, I will move the source code to my server and complete the project.

Target Market(s)

Residential Home Owners and Business Owners

Industry/Entity Type

Plumbing, Home Services, Remodeling, Construction

Coding

Coded - Design and coding required

Number of Pages Required

5+ page

Colors
0054AA
0677BA
7BADD7
CADEEF
E8F1F8
FFC000
F8CF3A
FAE287
FDF2CF
FEFAEE
EE7325
F08F49
F5BC92
FAE3D3
FDF4ED

Requirements
Must have
• Clean, colorful, and professional

```html
<!DOCTYPE html>
<html lang="en">
<head>
<meta charset="utf-8">
<title>Sir FlowBoiler – Modern Plumbing Concepts</title>
<link href="https://fonts.googleapis.com/css2?family=Hind:wght@400;500;600;700&family=Poppins:wght@400;500;600&family=Roboto+Condensed:wght@300;400&display=swap" rel="stylesheet">
<style>
:root{
  --blue:#0054AA;
  --blue-mid:#0677BA;
  --blue-soft:#CADEEF;
  --orange:#EE7325;
  --orange-soft:#FAE3D3;
  --cream:#F6F3EC;
  --ink:#1c1c1c;
  --muted:#5d5d5d;
  --white:#ffffff;
}
*{box-sizing:border-box;margin:0;padding:0}
html,body{width:1200px;height:5305px;overflow:hidden}
body{position:relative;font-family:"Poppins",sans-serif;color:var(--ink);background:var(--white)}
.abs{position:absolute}
.heading{font-family:"Hind",sans-serif;font-weight:600;font-size:34px;line-height:38px;color:var(--ink)}
.heading em{font-style:normal;color:var(--orange)}
.pill{position:absolute;height:30px;padding:0 14px 0 12px;border:1px solid #e4e0d6;border-radius:15px;background:var(--white);display:flex;align-items:center;gap:8px;font-size:10.5px;color:var(--blue);letter-spacing:.2px}
.pill svg{width:12px;height:12px}
.photo{position:absolute}
.arrow-btn{position:absolute;width:38px;height:38px;border-radius:50%;background:var(--white);display:flex;align-items:center;justify-content:center;box-shadow:0 2px 6px rgba(0,0,0,.08)}
.arrow-btn svg{width:16px;height:16px}

/* header */
.site-header{left:0;top:0;width:1200px;height:72px;background:var(--white)}
.brand{position:absolute;display:flex;align-items:center;gap:8px;font-family:"Hind",sans-serif;font-weight:700;color:var(--blue)}
.brand .dot{border-radius:50%;background:var(--orange)}
.site-header .brand{left:113px;top:16px;font-size:20px}
.site-header .brand .dot{width:30px;height:30px}
.nav a{position:absolute;top:27px;font-size:12.5px;font-weight:500;color:var(--ink);text-decoration:none}
.nav a.active{color:var(--orange)}
.dropdown{left:593px;top:72px;width:142px;height:99px;background:var(--white);box-shadow:0 4px 14px rgba(0,0,0,.12);border-top:2px solid var(--orange)}
.dropdown a{display:block;height:33px;line-height:33px;padding-left:12px;font-size:11px;color:var(--ink);text-decoration:none}

/* hero */
.hero{left:0;top:72px;width:1200px;height:323px;background:linear-gradient(90deg,var(--blue) 0,var(--blue) 614px,var(--orange) 614px)}
.hero .pill{left:117px;top:51px;background:var(--blue-mid);border-color:var(--blue-mid);color:var(--white)}
.hero h1{position:absolute;left:119px;top:100px;font-family:"Hind",sans-serif;font-weight:700;font-size:78px;line-height:74px;color:var(--white)}
.hero-media{left:74px;top:397px;width:1052px;height:471px;background:linear-gradient(100deg,#4c5561 0%,#7e8590 45%,#b9a58a 75%,#8d7a63 100%)}
.promise{position:absolute;left:58px;top:96px;list-style:none;font-family:"Roboto Condensed",sans-serif;font-weight:300;font-size:27px;line-height:50.5px;color:var(--white)}
.promise-note{position:absolute;left:66px;top:356px;font-size:11px;color:var(--white);letter-spacing:.2px}

/* about */
.about-photo{left:113px;top:961px;width:375px;height:457px;background:linear-gradient(160deg,#c9d3dc,#6f8aa5 55%,#3e4a57)}
.about .pill{left:589px;top:988px}
.about h2{position:absolute;left:584px;top:1035px}
.about .lead{position:absolute;left:584px;top:1128px;width:405px;font-size:11.5px;line-height:17.5px;color:var(--muted)}
.feature{left:584px;top:1235px;width:280px}
.feature h3{position:absolute;left:62px;top:2px;font-family:"Hind",sans-serif;font-weight:600;font-size:16px;color:var(--ink);white-space:nowrap}
.feature p{position:absolute;left:62px;top:28px;width:215px;font-size:11px;line-height:17px;color:var(--muted)}
.about-thumb{left:889px;top:1220px;width:177px;height:169px;background:linear-gradient(160deg,#7b8da0,#3c4a5c)}
.btn{position:absolute;display:flex;align-items:center;justify-content:center;gap:14px;border-radius:18px;background:var(--blue);color:var(--white);font-size:11px;font-weight:500;text-decoration:none}
.about .btn{left:584px;top:1340px;width:149px;height:35px}

/* services */
.services{left:0;top:1498px;width:1200px;height:626px;background:var(--cream)}
.services .pill{left:119px;top:89px}
.services h2{position:absolute;left:119px;top:140px}
.service-card{position:absolute;top:255px;width:305px;height:280px;background:var(--white)}
.service-card .icon{position:absolute;left:23px;top:28px;width:42px;height:56px}
.service-card h3{position:absolute;left:23px;top:128px;font-family:"Hind",sans-serif;font-weight:500;font-size:17px}
.service-card p{position:absolute;left:23px;top:168px;width:255px;font-size:11px;line-height:18px;color:var(--muted)}
.more{position:absolute;display:flex;align-items:center;gap:6px;font-size:10.5px;font-weight:600;color:var(--ink);text-decoration:none}
.more svg{width:12px;height:10px}
.service-card .more{left:23px;top:229px}

/* video */
.video{left:0;top:2124px;width:1200px;height:405px;background:linear-gradient(90deg,#3a3835 0%,#6d6a66 30%,#8a8784 50%,#3b4d78 75%,#2b2b2e 100%)}
.play{position:absolute;left:572px;top:187px;width:50px;height:34px;border-radius:8px;background:#e02b20;display:flex;align-items:center;justify-content:center}

/* why */
.why-band{left:873px;top:2529px;width:327px;height:640px;background:var(--blue)}
.why-photo{left:607px;top:2620px;width:473px;height:459px;background:linear-gradient(150deg,#e6e3de,#b9b3a9 40%,#4f6d96 80%)}
.why .pill{left:113px;top:2612px}
.why h2{position:absolute;left:113px;top:2660px}
.why .lead{position:absolute;left:113px;top:2752px;width:460px;font-size:11px;line-height:18px;color:var(--muted)}
.skill{position:absolute;left:113px;width:449px}
.skill span{font-size:12.5px;font-weight:500}
.skill b{position:absolute;top:0;font-size:12px;font-weight:400;color:var(--muted)}
.skill .track{position:absolute;top:27px;left:0;width:449px;height:5px;background:#e4e4e4;border-radius:3px}
.skill .fill{height:5px;background:var(--orange);border-radius:3px}

/* testimonials */
.testi .pill{left:117px;top:3250px}
.testi h2{position:absolute;left:119px;top:3302px}
.review{position:absolute;top:3420px;width:307px;height:173px;background:var(--cream)}
.review p{position:absolute;left:23px;top:28px;width:262px;font-size:11px;line-height:18.5px;color:var(--muted)}
.review .avatar{position:absolute;left:23px;top:106px;width:36px;height:36px;border-radius:50%;background:linear-gradient(#f1b58a,#c4662c)}
.review h4{position:absolute;left:78px;top:105px;font-size:12.5px;font-weight:500;color:var(--orange)}
.review small{position:absolute;left:78px;top:126px;font-size:10px;color:var(--muted)}
.review .stars{position:absolute;right:22px;top:112px;font-size:13px;letter-spacing:1px;color:var(--orange)}

/* quote */
.quote{left:0;top:3690px;width:428px;height:591px;background:var(--orange)}
.quote h2{position:absolute;left:45px;top:105px;font-family:"Hind",sans-serif;font-weight:600;font-size:31px;color:var(--white)}
.field{position:absolute;left:45px;width:332px;height:34px;border-bottom:1px solid rgba(255,255,255,.55);font-size:10.5px;color:var(--white);letter-spacing:.3px;padding:12px 0 0 14px}
.quote .btn{left:226px;top:457px;width:149px;height:34px}
.map{left:428px;top:3690px;width:772px;height:591px;background:linear-gradient(135deg,#b9d9cf 0%,#d6e6cf 40%,#cfe3d0 55%,#9fcbe0 100%)}

/* blog */
.blog .pill{left:533px;top:4340px}
.blog h2{position:absolute;left:0;top:4406px;width:1200px;text-align:center}
.post{position:absolute;top:4470px;height:362px;background:var(--cream)}
.post .thumb{position:absolute;left:23px;top:25px;right:23px;height:164px}
.post .date{position:absolute;right:23px;top:167px;width:40px;height:36px;background:var(--white);text-align:center;font-size:11px;line-height:13px;font-weight:600;padding-top:5px}
.post .meta{position:absolute;left:30px;top:220px;display:flex;gap:24px;font-size:10.5px;color:var(--muted)}
.post .meta span{display:flex;align-items:center;gap:6px}
.post .meta svg{width:11px;height:11px}
.post h3{position:absolute;left:23px;top:266px;width:260px;font-family:"Hind",sans-serif;font-weight:500;font-size:17px;line-height:24px}
.post .more{left:23px;top:330px}

/* footer */
.site-footer{left:0;top:4923px;width:1200px;height:382px;background:var(--blue);color:var(--white)}
.site-footer .brand{left:117px;top:80px;font-size:21px;color:var(--white)}
.site-footer .brand .dot{width:32px;height:32px}
.footer-about{position:absolute;left:117px;top:162px;width:215px;font-size:11px;line-height:17px}
.socials{position:absolute;left:117px;top:240px;display:flex;gap:13px}
.socials span{width:29px;height:29px;background:var(--orange);display:block}
.site-footer h4{position:absolute;top:82px;font-family:"Hind",sans-serif;font-weight:600;font-size:17px}
.links{position:absolute;left:362px;top:125px;list-style:none;font-size:11px;line-height:27.5px}
.links li::before{content:"—";margin-right:10px;opacity:.8}
.recent{position:absolute;left:605px;width:210px}
.recent .pic{position:absolute;left:0;top:0;width:58px;height:58px;background:linear-gradient(135deg,#9aa6b3,#4a5563)}
.recent p{position:absolute;left:70px;top:2px;width:140px;font-size:10px;line-height:13.5px}
.recent small{display:block;font-size:9.5px;opacity:.8;margin-top:2px}
.contact-item{position:absolute;left:848px;width:240px}
.contact-item svg{position:absolute;left:0;top:2px;width:26px;height:26px}
.contact-item b{position:absolute;left:42px;top:0;font-size:11px;font-weight:600}
.contact-item span{position:absolute;left:42px;top:20px;font-size:11px;white-space:nowrap}
.copyright{position:absolute;left:117px;top:353px;font-size:11px}
</style>
</head>
<body>

<header class="abs site-header">
  <div class="brand"><span class="dot"></span>Sir FlowBoiler</div>
  <nav class="nav">
    <a href="#" style="left:527px">Home</a>
    <a href="#" class="active" style="left:601px">Heaters ⌄</a>
    <a href="#" style="left:685px">About Us</a>
    <a href="#" style="left:776px">Contact Us</a>
    <a href="#" style="left:879px">Privacy Policy, Terms &amp; Conditons</a>
  </nav>
</header>

<section class="abs hero">
  <div class="pill"><svg viewBox="0 0 12 12"><path d="M6 1v10M1 6h10" stroke="#fff" stroke-width="2"/></svg>LET'S GET TO WORK</div>
  <h1>Modern Plumbing<br>Concepts</h1>
</section>

<div class="abs dropdown">
  <a href="#">Gas Water Heaters</a>
  <a href="#">Electric Water Heaters</a>
  <a href="#">Tankless Water Heaters</a>
</div>

<div class="photo hero-media" role="img" aria-label="Smiling plumber in hard hat with coffee and phone in a workshop">
  <ul class="promise">
    <li>- Same Day Service</li>
    <li>- Best Price Guarantee</li>
    <li>- 100% Satisfaction Rating</li>
    <li>- 15 Years warranty on Water Heater &amp; Parts</li>
    <li>- Life time warranty on Workmanship</li>
  </ul>
  <p class="promise-note">*ALL WARRANTIES ARE TRANSFERRABLE UPON HOME SALE</p>
</div>

<section class="about">
  <div class="photo about-photo" role="img" aria-label="Plumber in gloves fitting pipes under a water heater"></div>
  <div class="pill"><svg viewBox="0 0 12 12"><path d="M6 1v10M1 6h10" stroke="#0054AA" stroke-width="2"/></svg>ABOUT OUR COMPANY</div>
  <h2 class="heading">Platform To Enhance Water<br><em>Heaters</em> Solutions</h2>
  <p class="lead">Lorem ipsum dolor sit amet, consectetur adipiscing elit, sed do eiusmod tempor incididunt ut labore et dolore magna aliqua. Ut enim ad minim veniam, quis nostrud exercitation ullamco laboris nisi</p>
  <div class="abs feature">
    <svg width="46" height="46" viewBox="0 0 46 46" fill="none" stroke="#1c1c1c" stroke-width="2"><rect x="8" y="14" width="30" height="16" rx="3"/><path d="M4 18h4M38 18h4M4 26h4M38 26h4M14 30v8M32 30v8M10 38h26M16 6v8M30 6v8M23 4v10"/></svg>
    <h3>Modern Technology</h3>
    <p>Sollicitudin loremt quis bibendum nisl elit consequat ipsum.</p>
  </div>
  <div class="photo about-thumb" role="img" aria-label="Technician repairing a sink fitting"></div>
  <a href="#" class="btn">ABOUT US <svg width="16" height="12" viewBox="0 0 16 12"><path d="M1 6h13M9 1l5 5-5 5" stroke="#fff" stroke-width="1.8" fill="none"/></svg></a>
</section>

<section class="abs services">
  <div class="pill"><svg viewBox="0 0 12 12"><path d="M6 1v10M1 6h10" stroke="#0054AA" stroke-width="2"/></svg>OUR POPULAR SERVICES</div>
  <h2 class="heading">Building Trust Through<br>Quality <em>Service</em></h2>
  <div class="arrow-btn" style="left:971px;top:160px"><svg viewBox="0 0 16 16"><path d="M14 8H2M7 3L2 8l5 5" stroke="#1c1c1c" stroke-width="1.6" fill="none"/></svg></div>
  <div class="arrow-btn" style="left:1024px;top:160px"><svg viewBox="0 0 16 16"><path d="M2 8h12M9 3l5 5-5 5" stroke="#1c1c1c" stroke-width="1.6" fill="none"/></svg></div>

  <article class="service-card" style="left:117px">
    <svg class="icon" viewBox="0 0 42 56" fill="none" stroke="#1c1c1c" stroke-width="2"><rect x="4" y="2" width="34" height="44" rx="4"/><rect x="11" y="10" width="20" height="18" rx="2"/><path d="M21 24c-4 0-5-3-3-7 1 2 2 2 3 0 2 3 3 7 0 7z"/><circle cx="21" cy="37" r="3"/><path d="M14 46v8M28 46v8"/></svg>
    <h3>Gas Water Heaters</h3>
    <p>Proin gravida nibh vel velit auctor aliquet. Sollicitudin,</p>
    <a href="#" class="more">READ MORE <svg viewBox="0 0 12 10"><path d="M1 5h9M6 1l4 4-4 4" stroke="#1c1c1c" stroke-width="1.5" fill="none"/></svg></a>
  </article>
  <article class="service-card" style="left:440px">
    <svg class="icon" viewBox="0 0 42 56" fill="none" stroke="#1c1c1c" stroke-width="2"><rect x="6" y="2" width="30" height="44" rx="6"/><circle cx="21" cy="14" r="5"/><path d="M21 12v3"/><path d="M14 46v8M28 46v8"/></svg>
    <h3>Electric Water Heaters</h3>
    <p>Proin gravida nibh vel velit auctor aliquet. Sollicitudin,</p>
    <a href="#" class="more">READ MORE <svg viewBox="0 0 12 10"><path d="M1 5h9M6 1l4 4-4 4" stroke="#1c1c1c" stroke-width="1.5" fill="none"/></svg></a>
  </article>
  <article class="service-card" style="left:761px">
    <svg class="icon" viewBox="0 0 42 56" fill="none" stroke="#1c1c1c" stroke-width="2"><rect x="4" y="2" width="26" height="40" rx="4"/><circle cx="17" cy="12" r="3"/><rect x="10" y="22" width="14" height="10" rx="2"/><path d="M34 20c3 3 3 7 0 10M38 16c5 5 5 13 0 18M12 42v8M22 42v8"/></svg>
    <h3>Tankless Water Heaters</h3>
    <p>Proin gravida nibh vel velit auctor aliquet. Sollicitudin,</p>
    <a href="#" class="more">READ MORE <svg viewBox="0 0 12 10"><path d="M1 5h9M6 1l4 4-4 4" stroke="#1c1c1c" stroke-width="1.5" fill="none"/></svg></a>
  </article>
</section>

<section class="abs video" role="img" aria-label="Technician standing beside tank and tankless water heaters in a warehouse">
  <div class="play"><svg width="14" height="16" viewBox="0 0 14 16"><path d="M1 1l12 7-12 7z" fill="#fff"/></svg></div>
</section>

<section class="why">
  <div class="abs why-band"></div>
  <div class="photo why-photo" role="img" aria-label="Plumber lying under a kitchen sink fixing the drain"></div>
  <div class="pill"><svg viewBox="0 0 12 12"><path d="M6 1v10M1 6h10" stroke="#0054AA" stroke-width="2"/></svg>WHY CHOOSE US</div>
  <h2 class="heading">Modern Plumbing<br>Challenges &amp; <em>Solutions</em></h2>
  <p class="lead">Lorem ipsum dolor sit amet, consectetur adipiscing elit, eiusmod tempor incididunt ut labore et dolore magna aliqua.</p>
  <div class="skill" style="top:2808px"><span>Gas Water Heaters</span><b style="left:393px">88%</b><div class="track"><div class="fill" style="width:88%"></div></div></div>
  <div class="skill" style="top:2868px"><span>Electric Water Heaters</span><b style="left:320px">78%</b><div class="track"><div class="fill" style="width:78%"></div></div></div>
  <div class="skill" style="top:2922px"><span>Tankless Water Heaters</span><b style="left:395px">95%</b><div class="track"><div class="fill" style="width:95%"></div></div></div>
</section>

<section class="testi">
  <div class="pill"><svg viewBox="0 0 12 12"><path d="M6 1v10M1 6h10" stroke="#0054AA" stroke-width="2"/></svg>TESTIMONIALS</div>
  <h2 class="heading">Feedback That Builds Future<br>Client <em>Highlights</em></h2>
  <div class="arrow-btn" style="left:994px;top:3321px"><svg viewBox="0 0 16 16"><path d="M14 8H2M7 3L2 8l5 5" stroke="#1c1c1c" stroke-width="1.6" fill="none"/></svg></div>
  <div class="arrow-btn" style="left:1039px;top:3321px"><svg viewBox="0 0 16 16"><path d="M2 8h12M9 3l5 5-5 5" stroke="#1c1c1c" stroke-width="1.6" fill="none"/></svg></div>

  <article class="review" style="left:117px">
    <p>Lorem ipsum dolor sit amet, consectetur adipiscing elit, eiusmod tempor incididunt ut labore et dolore magna aliqua.</p>
    <div class="avatar" role="img" aria-label="Client portrait"></div>
    <h4>Derek L. Hanson</h4><small>Experts</small><span class="stars">★★★★★</span>
  </article>
  <article class="review" style="left:445px">
    <p>Lorem ipsum dolor sit amet, consectetur adipiscing elit, eiusmod tempor incididunt ut labore et dolore magna aliqua.</p>
    <div class="avatar" role="img" aria-label="Client portrait"></div>
    <h4>Maria P. Dunne</h4><small>Experts</small><span class="stars">★★★★★</span>
  </article>
  <article class="review" style="left:772px">
    <p>Lorem ipsum dolor sit amet, consectetur adipiscing elit, eiusmod tempor incididunt ut labore et dolore magna aliqua.</p>
    <div class="avatar" role="img" aria-label="Client portrait"></div>
    <h4>Evan Porter</h4><small>Experts</small><span class="stars">★★★★★</span>
  </article>
</section>

<section class="abs quote">
  <h2>Quote Request Form</h2>
  <div class="field" style="top:177px">FIRST NAME</div>
  <div class="field" style="top:223px">LAST NAME</div>
  <div class="field" style="top:270px">EMAIL ADDRESS</div>
  <div class="field" style="top:316px">PHONE #</div>
  <div class="field" style="top:364px;height:82px">MESSAGE</div>
  <a href="#" class="btn">SUBMIT <svg width="16" height="12" viewBox="0 0 16 12"><path d="M1 6h13M9 1l5 5-5 5" stroke="#fff" stroke-width="1.8" fill="none"/></svg></a>
</section>
<div class="photo map" role="img" aria-label="Regional map highlighting the company's coastal service area"></div>

<section class="blog">
  <div class="pill"><svg viewBox="0 0 12 12"><path d="M6 1v10M1 6h10" stroke="#0054AA" stroke-width="2"/></svg>LATEST NEWS</div>
  <h2 class="heading">Read Our Latest News &amp; <em>Blog</em></h2>

  <article class="post" style="left:128px;width:306px">
    <div class="thumb" role="img" aria-label="Plumber working under a sink" style="background:linear-gradient(135deg,#c8ccd0,#7f8c99 50%,#3f4d5f)"></div>
    <div class="date">25<br>Dec</div>
    <div class="meta"><span><svg viewBox="0 0 12 12"><circle cx="6" cy="4" r="2.5" fill="#5d5d5d"/><path d="M1 12c0-3 2-5 5-5s5 2 5 5z" fill="#5d5d5d"/></svg>John</span><span><svg viewBox="0 0 12 12"><rect x="1" y="2" width="10" height="7" fill="none" stroke="#5d5d5d"/></svg>Comments 0</span></div>
    <h3>Lorem Ipsum. "Neque porro quisquam est qui dolorem</h3>
    <a href="#" class="more">Read More <svg viewBox="0 0 12 10"><path d="M1 5h9M6 1l4 4-4 4" stroke="#1c1c1c" stroke-width="1.5" fill="none"/></svg></a>
  </article>
  <article class="post" style="left:451px;width:302px">
    <div class="thumb" role="img" aria-label="Hands fitting a pipe joint" style="background:linear-gradient(135deg,#8c8f92,#4f545b 50%,#2f3237)"></div>
    <div class="date">25<br>Dec</div>
    <div class="meta"><span><svg viewBox="0 0 12 12"><circle cx="6" cy="4" r="2.5" fill="#5d5d5d"/><path d="M1 12c0-3 2-5 5-5s5 2 5 5z" fill="#5d5d5d"/></svg>Mandy</span><span><svg viewBox="0 0 12 12"><rect x="1" y="2" width="10" height="7" fill="none" stroke="#5d5d5d"/></svg>Comments 0</span></div>
    <h3>Lorem Ipsum. "Neque porro quisquam est qui</h3>
    <a href="#" class="more">Read More <svg viewBox="0 0 12 10"><path d="M1 5h9M6 1l4 4-4 4" stroke="#1c1c1c" stroke-width="1.5" fill="none"/></svg></a>
  </article>
  <article class="post" style="left:770px;width:300px">
    <div class="thumb" role="img" aria-label="Technician servicing a wall-mounted heater" style="background:linear-gradient(135deg,#b8c4d0,#5e7790 50%,#c46a30)"></div>
    <div class="date">23<br>Dec</div>
    <div class="meta"><span><svg viewBox="0 0 12 12"><circle cx="6" cy="4" r="2.5" fill="#5d5d5d"/><path d="M1 12c0-3 2-5 5-5s5 2 5 5z" fill="#5d5d5d"/></svg>Ocemean</span><span><svg viewBox="0 0 12 12"><rect x="1" y="2" width="10" height="7" fill="none" stroke="#5d5d5d"/></svg>Comments 0</span></div>
    <h3>Lorem Ipsum. "Neque porro quisquam est</h3>
    <a href="#" class="more">Read More <svg viewBox="0 0 12 10"><path d="M1 5h9M6 1l4 4-4 4" stroke="#1c1c1c" stroke-width="1.5" fill="none"/></svg></a>
  </article>
</section>

<footer class="abs site-footer">
  <div class="brand"><span class="dot"></span>Sir FlowBoiler</div>
  <p class="footer-about">Sedut perspiciatis unde omnis iste natus error sitlutem acc usantium doloremque</p>
  <div class="socials"><span></span><span></span><span></span><span></span></div>

  <h4 style="left:362px">Our Service</h4>
  <ul class="links">
    <li>Our Services</li>
    <li>Gas Water Heaters</li>
    <li>Electric Water Heaters</li>
    <li>Tankless Water Heaters</li>
    <li>Repair Services</li>
  </ul>

  <h4 style="left:605px">Recent Post</h4>
  <div class="recent" style="top:129px"><div class="pic" role="img" aria-label="Post thumbnail"></div><p>Lorem Ipsum. "Neque porro quisquam est qui dolorem<small>December 24, 2025</small></p></div>
  <div class="recent" style="top:215px"><div class="pic" role="img" aria-label="Post thumbnail"></div><p>Lorem Ipsum. "Neque porro quisquam est qui dolorem<small>December 21, 2025</small></p></div>

  <h4 style="left:848px">Quick Contact</h4>
  <div class="contact-item" style="top:126px"><svg viewBox="0 0 26 26"><path d="M13 3L2 12h3v10h6v-6h4v6h6V12h3z" fill="#fff"/></svg><b>Address:</b><span>Seabright County, Marlow</span></div>
  <div class="contact-item" style="top:174px"><svg viewBox="0 0 26 26"><path d="M7 3l4 5-2 3c1 3 3 5 6 6l3-2 5 4-2 4C12 23 3 14 3 6z" fill="#fff"/></svg><b>Telephone:</b><span>555 0142 7788</span></div>
  <div class="contact-item" style="top:222px"><svg viewBox="0 0 26 26" fill="none" stroke="#fff" stroke-width="1.6"><circle cx="13" cy="13" r="10"/><ellipse cx="13" cy="13" rx="4.5" ry="10"/><path d="M3 13h20M5 8h16M5 18h16"/></svg><b>Email:</b><span>hello@sirflowboiler.com</span></div>

  <p class="copyright">Copyright © SirFlowBoiler rights reserved.</p>
</footer>

</body>
</html>
```